Business Card Design Project

Crestline Vein Center

Dr Tomas Venrick M.D, F.R.C.S
Vascular and Vein Surgery

47-18 Pellham Avenue, Suite 314
Astoria
NY 11287

212-555-0147
718-555-0193
www.crestlinecare.us back of the card for scheduled appointments up to 5 appointment dates

Target Market(s)

Male and Female patients from 25 onwards with spider veins or varicose veins

Industry/Entity Type

Business

Font styles to use
Serif

Colors
86cae6
85abd2
0456a4

Requirements
Must have
• Modern Sophisticated design using light blue and grey text
Should not have
• hearts or flowers

```html
<!DOCTYPE html>
<html lang="en">
<head>
<meta charset="utf-8">
<title>Crestline Vein Center – Business Card</title>
<link href="https://fonts.googleapis.com/css2?family=PT+Sans:wght@400;700&display=swap" rel="stylesheet">
<style>
  :root{
    --deep-blue:#0456a4;
    --mid-blue:#1a74c4;
    --sky-blue:#86cae6;
    --soft-blue:#85abd2;
    --navy:#123e7a;
    --paper:#ffffff;
    --paper-shade:#dfe6ef;
    --grey-text:#7a808a;
    --rule:#555b63;
    --backdrop:#e9ebee;
  }
  *{margin:0;padding:0;box-sizing:border-box}
  html,body{width:704px;height:1200px;overflow:hidden}
  body{background:var(--backdrop);font-family:"PT Sans",sans-serif;position:relative}

  .card{position:absolute;left:72px;width:560px;height:320px;border-radius:16px;overflow:hidden;
        background:var(--paper);box-shadow:0 6px 18px rgba(0,0,0,.18)}
  .card-front{top:140px}
  .card-back{top:740px}
  .card-art{position:absolute;inset:0}

  .brand{position:absolute;display:flex;align-items:center;gap:14px}
  .brand-mark{width:62px;height:62px;border:4px solid var(--mid-blue);background:var(--paper)}
  .brand-name{font-size:27px;font-weight:700;color:var(--mid-blue);line-height:1}
  .brand-name small{font-size:13px;font-weight:400;color:var(--soft-blue);margin-left:4px}
  .brand-specialty{font-size:15px;color:var(--grey-text);margin-top:4px}
  .card-front .brand{left:40px;top:78px}

  .address{position:absolute;left:40px;top:218px;color:var(--paper);font-size:15px;line-height:1.35;display:flex;gap:10px}
  .address svg{margin-top:3px;flex:none}
  .contacts{position:absolute;right:34px;top:222px;color:var(--paper);font-size:14px;line-height:1.45;text-align:right}
  .contacts li{list-style:none;display:flex;justify-content:flex-end;align-items:center;gap:8px}
  .contacts svg{flex:none}

  .card-back .brand{right:36px;top:24px;gap:10px}
  .card-back .brand-mark{width:46px;height:46px;border-width:3px}
  .card-back .brand-name{font-size:20px}
  .card-back .brand-name small{font-size:10px}
  .card-back .brand-specialty{font-size:12px;margin-top:2px}
  .appointment-title{position:absolute;left:40px;top:96px;font-size:22px;color:var(--mid-blue)}
  .appointment-list{position:absolute;left:40px;top:134px;list-style:none}
  .appointment-list li{display:flex;align-items:flex-end;font-size:15px;color:var(--grey-text);height:27px}
  .appointment-list .line{display:inline-block;border-bottom:1px solid var(--rule);margin:0 6px 4px 4px}
  .line-date{width:150px}
  .line-time{width:120px}
</style>
</head>
<body>

<section class="card card-front" aria-label="Card front">
  <svg class="card-art" viewBox="0 0 560 320" aria-hidden="true">
    <defs>
      <linearGradient id="blueBand" x1="0" y1="0" x2="1" y2="0">
        <stop offset="0" stop-color="#0456a4"/><stop offset="1" stop-color="#1a74c4"/>
      </linearGradient>
    </defs>
    <rect width="560" height="54" fill="url(#blueBand)"/>
    <path d="M0 196 C160 196 330 214 440 182 C500 164 530 150 560 146 L560 320 L0 320 Z" fill="#85abd2"/>
    <path d="M0 206 C160 206 330 224 440 192 C500 174 530 160 560 156 L560 320 L0 320 Z" fill="#123e7a"/>
    <path d="M0 212 C160 212 330 230 440 198 C500 180 530 166 560 162 L560 320 L0 320 Z" fill="url(#blueBand)"/>
  </svg>

  <div class="brand">
    <span class="brand-mark"></span>
    <div>
      <div class="brand-name">Dr Tomas Venrick<small>M.D, F.R.C.S</small></div>
      <div class="brand-specialty">Vascular and Vein Surgery</div>
    </div>
  </div>

  <div class="address">
    <svg width="12" height="16" viewBox="0 0 12 16"><path d="M6 0a6 6 0 0 0-6 6c0 4.5 6 10 6 10s6-5.5 6-10a6 6 0 0 0-6-6zm0 8.5A2.5 2.5 0 1 1 6 3.5a2.5 2.5 0 0 1 0 5z" fill="#ffffff"/></svg>
    <div>47-18 Pellham Avenue, Suite 314<br>Astoria<br>NY 11287</div>
  </div>

  <ul class="contacts">
    <li>212-555-0147
      <svg width="13" height="13" viewBox="0 0 13 13"><rect width="13" height="13" rx="2" fill="#ffffff"/><path d="M4 3c.6 0 1 1.6 1 2s-.8.6-.6 1.2a4 4 0 0 0 2.4 2.4c.6.2.8-.6 1.2-.6s2 .4 2 1-.8 1.2-1.6 1.2A6 6 0 0 1 2.8 4.6C2.8 3.8 3.4 3 4 3z" fill="#0456a4"/></svg>
    </li>
    <li>718-555-0193
      <svg width="13" height="13" viewBox="0 0 13 13"><rect width="13" height="13" rx="2" fill="none"/></svg>
    </li>
    <li>www.crestlinecare.us
      <svg width="13" height="13" viewBox="0 0 13 13"><circle cx="6.5" cy="6.5" r="5.5" fill="none" stroke="#ffffff" stroke-width="1.3"/><path d="M1 6.5h11M6.5 1c-3 3.5-3 7.5 0 11M6.5 1c3 3.5 3 7.5 0 11" fill="none" stroke="#ffffff" stroke-width="1"/></svg>
    </li>
  </ul>
</section>

<section class="card card-back" aria-label="Card back">
  <svg class="card-art" viewBox="0 0 560 320" aria-hidden="true">
    <path d="M560 72 C535 150 505 235 425 290 C365 318 200 316 0 318 L0 320 L560 320 Z" fill="#85abd2"/>
    <path d="M560 130 C542 200 515 262 465 298 C450 308 435 315 420 320 L560 320 Z" fill="#dfe6ef"/>
    <path d="M560 60 C535 140 505 225 420 280 C360 310 200 310 0 312" fill="none" stroke="#123e7a" stroke-width="5"/>
  </svg>

  <div class="brand">
    <span class="brand-mark"></span>
    <div>
      <div class="brand-name">Dr Tomas Venrick<small>M.D, F.R.C.S</small></div>
      <div class="brand-specialty">Vascular and Vein Surgery</div>
    </div>
  </div>

  <h2 class="appointment-title">Your Next Appointment</h2>
  <ul class="appointment-list">
    <li>Date<span class="line line-date"></span>Time<span class="line line-time"></span></li>
    <li>Date<span class="line line-date"></span>Time<span class="line line-time"></span></li>
    <li>Date<span class="line line-date"></span>Time<span class="line line-time"></span></li>
    <li>Date<span class="line line-date"></span>Time<span class="line line-time"></span></li>
    <li>Date<span class="line line-date"></span>Time<span class="line line-time"></span></li>
  </ul>
</section>

</body>
</html>
```